Calder Pizza - Takeout Menu Design

We are looking for a takeout menu design.
We are looking for a( 5" x 8.5" DOUBLE SIDED) flyer with our available pizza flavors
Must be easy to ready and not "busy"

Must include our logo (attached)
website: www.calderpizza.ca
address:
Fenwick Ridge Plaza
417, 318 9 Avenue SW
and the following details:
Visit our website for our complete appetizer, pasta, salad and catering menu.

Winner of this contest will also be offered to create a few print designs via printhive.

Please do not hesitate to ask any questions.

Target Market(s)

Business / Office clientele

Industry/Entity Type

Pizza place / specializing in corporate orders

Requirements
Must have
• Easy to read
Should not have
• Can not be busy or cluttered

```html
<!DOCTYPE html>
<html lang="en">
<head>
<meta charset="utf-8">
<title>Calder Pizza – Take-Out Menu</title>
<link rel="stylesheet" href="https://fonts.googleapis.com/css2?family=Quicksand:wght@400;500;600;700&display=swap">
<style>
  :root {
    --red: #c0302a;
    --ink: #222222;
    --ink-soft: #333333;
    --paper: #efefef;
    --paper-light: #f6f6f6;
    --canvas: #ffffff;
    --sketch-tone: #e3d6c8;
    --dots: #555555;
  }
  * { margin: 0; padding: 0; box-sizing: border-box; }
  html, body { width: 1200px; height: 848px; overflow: hidden; background: var(--canvas); }
  body { position: relative; font-family: "Quicksand", sans-serif; color: var(--ink); }

  .page {
    position: absolute;
    background: linear-gradient(90deg, var(--paper) 0%, var(--paper-light) 50%, var(--paper) 100%);
    box-shadow: 8px 10px 14px rgba(0,0,0,0.28);
    overflow: hidden;
  }
  .page--front { left: 111px; top: 41px; width: 440px; height: 746px; }
  .page--back { left: 643px; top: 41px; width: 445px; height: 752px; }

  .brand {
    position: absolute; left: 0; width: 100%; top: 38px;
    text-align: center; font-size: 52px; font-weight: 500;
    letter-spacing: 1px; color: var(--ink); line-height: 1;
  }
  .tagline {
    position: absolute; left: 0; width: 100%; top: 121px;
    text-align: center; font-style: italic; font-size: 17px;
    line-height: 21px; color: var(--ink-soft); font-weight: 500;
  }

  .section-band { position: absolute; left: 8px; width: 250px; height: 28px; }
  .section-band svg { position: absolute; inset: 0; }
  .section-band span {
    position: relative; display: block; text-align: center;
    color: #fff; font-weight: 700; font-size: 16px; line-height: 28px;
  }
  .size-head {
    position: absolute; color: var(--red); font-weight: 700; font-size: 17px; line-height: 1;
  }

  .item { position: absolute; }
  .page--front .item { left: 13px; width: 392px; }
  .page--back .item { left: 12px; width: 400px; }
  .item-line { display: flex; align-items: baseline; font-size: 12.5px; line-height: 14px; font-weight: 500; }
  .item-line::before { content: "•"; color: var(--red); width: 7px; flex: none; font-size: 11px; }
  .item-name { flex: none; color: var(--ink); }
  .leader { flex: 1; border-bottom: 1px dotted var(--dots); margin: 0 3px 3px 4px; }
  .price-small { flex: none; width: 60px; }
  .price-large { flex: none; width: 38px; }
  .page--front .price-small { width: 62px; }
  .item-desc { padding-left: 7px; font-size: 9.6px; line-height: 11.5px; color: var(--ink-soft); font-weight: 500; }

  .torn { position: absolute; left: 0; width: 100%; }

  .sketch-veg {
    position: absolute; left: 13px; top: 10px; width: 72px; height: 74px;
    background: radial-gradient(circle at 50% 55%, var(--sketch-tone), rgba(227,214,200,0));
    border-radius: 40%;
  }
  .sketch-pizza {
    position: absolute; left: 98px; top: 463px; width: 265px; height: 130px;
    background: linear-gradient(180deg, var(--sketch-tone), #d9b98a);
    border-radius: 135px 135px 0 0;
  }

  .promo {
    position: absolute; left: 0; width: 100%; color: #fff; text-align: center;
  }
  .promo-lead { top: 604px; font-style: italic; font-size: 15.5px; line-height: 18px; font-weight: 500; }
  .promo-url { top: 650px; font-size: 24px; font-weight: 700; }
  .promo-address { top: 689px; font-size: 13.5px; line-height: 16px; font-weight: 500; }
</style>
</head>
<body>

<section class="page page--front">
  <div class="brand">CALDER PIZZA</div>
  <p class="tagline">All of our pizzas are prepared fresh everyday using<br>only the finest mozzarella blend and ingredients.</p>

  <div class="section-band" style="top:203px">
    <svg viewBox="0 0 250 28" preserveAspectRatio="none"><polygon fill="#c0302a" points="4,3 246,1 238,8 250,12 240,17 248,24 6,27 10,21 0,16 8,11 0,6"/></svg>
    <span>Classic Take-Out Pizza</span>
  </div>
  <div class="size-head" style="left:314px;top:209px">8"</div>
  <div class="size-head" style="left:370px;top:209px">13"</div>

  <div class="item" style="top:244px"><div class="item-line"><span class="item-name">Pepperoni &amp; Mushroom</span><span class="leader"></span><span class="price-small">$12.99</span><span class="price-large">$30.95</span></div></div>
  <div class="item" style="top:259px"><div class="item-line"><span class="item-name">Pepperoni</span><span class="leader"></span><span class="price-small">$11.99</span><span class="price-large">$29.95</span></div></div>
  <div class="item" style="top:273px"><div class="item-line"><span class="item-name">Hawaiian</span><span class="leader"></span><span class="price-small">$12.99</span><span class="price-large">$30.95</span></div></div>
  <div class="item" style="top:288px"><div class="item-line"><span class="item-name">Beef &amp; Mushroom</span><span class="leader"></span><span class="price-small">$13.49</span><span class="price-large">$32.95</span></div></div>
  <div class="item" style="top:303px"><div class="item-line"><span class="item-name">Pepperoni &amp; Ham</span><span class="leader"></span><span class="price-small">$12.99</span><span class="price-large">$30.95</span></div></div>
  <div class="item" style="top:317px"><div class="item-line"><span class="item-name">Ham &amp; Mushroom</span><span class="leader"></span><span class="price-small">$12.99</span><span class="price-large">$30.95</span></div></div>
  <div class="item" style="top:332px"><div class="item-line"><span class="item-name">Beef &amp; Onion</span><span class="leader"></span><span class="price-small">$13.49</span><span class="price-large">$32.95</span></div></div>
  <div class="item" style="top:347px"><div class="item-line"><span class="item-name">Cheese</span><span class="leader"></span><span class="price-small">$11.99</span><span class="price-large">$29.95</span></div></div>

  <div class="section-band" style="top:389px">
    <svg viewBox="0 0 250 28" preserveAspectRatio="none"><polygon fill="#c0302a" points="6,2 244,1 236,7 250,12 240,17 248,25 4,27 10,21 0,15 8,10 0,5"/></svg>
    <span>Specialty Take-Out Pizza</span>
  </div>
  <div class="size-head" style="left:316px;top:395px">8"</div>
  <div class="size-head" style="left:372px;top:395px">13"</div>

  <div class="item" style="top:423px"><div class="item-line"><span class="item-name">All Meat</span><span class="leader"></span><span class="price-small">$13.99</span><span class="price-large">$33.95</span></div><p class="item-desc">Pepperoni, Beef &amp; Smoked Ham</p></div>
  <div class="item" style="top:455px"><div class="item-line"><span class="item-name">Meat Supreme</span><span class="leader"></span><span class="price-small">$14.99</span><span class="price-large">$35.95</span></div><p class="item-desc">Pepperoni, Beef, Salami, Smoked Ham &amp; Bacon</p></div>
  <div class="item" style="top:486px"><div class="item-line"><span class="item-name">BBQ Chicken</span><span class="leader"></span><span class="price-small">$13.99</span><span class="price-large">$33.95</span></div><p class="item-desc">Chicken Breast, Hickory BBQ Sauce &amp; Red Onions</p></div>
  <div class="item" style="top:518px"><div class="item-line"><span class="item-name">Spicy BBQ Chicken</span><span class="leader"></span><span class="price-small">$14.49</span><span class="price-large">$35.95</span></div><p class="item-desc">Chicken Breast, Hickory BBQ Sauce, Red Onions<br>&amp; Banana Peppers</p></div>
  <div class="item" style="top:561px"><div class="item-line"><span class="item-name">Deluxe</span><span class="leader"></span><span class="price-small">$14.49</span><span class="price-large">$34.95</span></div><p class="item-desc">Pepperoni, Mushrooms, Ham, Tomatoes, Green Peppers<br>and Red Onions</p></div>
  <div class="item" style="top:603px"><div class="item-line"><span class="item-name">Double Pepperoni</span><span class="leader"></span><span class="price-small">$13.49</span><span class="price-large">$32.95</span></div><p class="item-desc">Loads of Pepperoni</p></div>
  <div class="item" style="top:635px"><div class="item-line"><span class="item-name">Four Cheese</span><span class="leader"></span><span class="price-small">$13.49</span><span class="price-large">$32.95</span></div><p class="item-desc">Mozzarella, Feta, Romano and Cheddar Cheese</p></div>
  <div class="item" style="top:666px"><div class="item-line"><span class="item-name">Greek</span><span class="leader"></span><span class="price-small">$13.99</span><span class="price-large">$33.95</span></div><p class="item-desc">Feta Cheese, Tomato, Green Peppers, Red Onions<br>and Black Olives</p></div>

  <svg class="torn" style="top:696px;height:50px" viewBox="0 0 440 50" preserveAspectRatio="none">
    <polygon fill="#c0302a" points="0,5 20,10 35,14 50,22 68,28 80,24 96,22 112,18 128,14 140,22 160,20 178,24 196,19 214,22 232,18 250,20 266,14 282,16 300,12 316,20 330,14 345,6 356,4 370,12 388,16 404,22 420,20 440,16 440,50 0,50"/>
  </svg>
</section>

<section class="page page--back">
  <div class="sketch-veg" role="img" aria-label="Hand-drawn sketch of mushroom, onion, tomato and pepper"></div>

  <div class="size-head" style="left:325px;top:60px">8"</div>
  <div class="size-head" style="left:386px;top:60px">13"</div>

  <div class="item" style="top:102px"><div class="item-line"><span class="item-name">Greek Supreme</span><span class="leader"></span><span class="price-small">$14.99</span><span class="price-large">$35.95</span></div><p class="item-desc">Chicken Breast, Feta Cheese, Tomato, Green Pepper,<br>Red Onions &amp; Black Olives</p></div>
  <div class="item" style="top:140px"><div class="item-line"><span class="item-name">Mediterranean Chicken</span><span class="leader"></span><span class="price-small">$14.79</span><span class="price-large">$35.95</span></div><p class="item-desc">Seasoned Chicken Breast, Tomatoes, Red Onions<br>and Feta Cheese</p></div>
  <div class="item" style="top:178px"><div class="item-line"><span class="item-name">Montreal</span><span class="leader"></span><span class="price-small">$13.49</span><span class="price-large">$32.95</span></div><p class="item-desc">Pepperoni &amp; Double Smoked Bacon</p></div>
  <div class="item" style="top:204px"><div class="item-line"><span class="item-name">Athenean</span><span class="leader"></span><span class="price-small">$14.49</span><span class="price-large">$34.95</span></div><p class="item-desc">Chicken Breast, Spinach, Feta Cheese and Tomato</p></div>
  <div class="item" style="top:231px"><div class="item-line"><span class="item-name">Supreme</span><span class="leader"></span><span class="price-small">$13.49</span><span class="price-large">$32.95</span></div><p class="item-desc">Pepperoni, Mushrooms &amp; Green Peppers</p></div>
  <div class="item" style="top:257px"><div class="item-line"><span class="item-name">Canadian</span><span class="leader"></span><span class="price-small">$13.49</span><span class="price-large">$32.95</span></div><p class="item-desc">Pepperoni, Mushrooms &amp; Ham</p></div>
  <div class="item" style="top:283px"><div class="item-line"><span class="item-name">Original Spinach</span><span class="leader"></span><span class="price-small">$13.49</span><span class="price-large">$32.95</span></div><p class="item-desc">Spinach &amp; Feta Cheese</p></div>
  <div class="item" style="top:310px"><div class="item-line"><span class="item-name">Chicken Club</span><span class="leader"></span><span class="price-small">$14.79</span><span class="price-large">$35.95</span></div><p class="item-desc">Chicken Breast, Double Smoked Bacon, Red Onions<br>and Tomatoes</p></div>
  <div class="item" style="top:348px"><div class="item-line"><span class="item-name">Zeus</span><span class="leader"></span><span class="price-small">$13.95</span><span class="price-large">$33.95</span></div><p class="item-desc">Spinach, Feta Cheese and Tomatoes</p></div>
  <div class="item" style="top:374px"><div class="item-line"><span class="item-name">Vegetarian</span><span class="leader"></span><span class="price-small">$13.49</span><span class="price-large">$32.95</span></div><p class="item-desc">Mushrooms, Tomatoes, Green Peppers<br>and Black Olives</p></div>
  <div class="item" style="top:412px"><div class="item-line"><span class="item-name">Calder Special</span><span class="leader"></span><span class="price-small">$14.49</span><span class="price-large">$34.95</span></div><p class="item-desc">Pepperoni, Mushrooms, Ham, Green Peppers<br>and Black Olives</p></div>

  <div class="sketch-pizza" role="img" aria-label="Hand-drawn sketch of a sliced pizza with toppings"></div>

  <svg class="torn" style="top:522px;height:230px" viewBox="0 0 445 230" preserveAspectRatio="none">
    <polygon fill="#c0302a" points="0,2 14,0 30,8 42,12 58,10 72,22 90,30 104,26 118,34 132,40 146,44 160,36 172,40 186,30 200,34 214,26 228,30 242,22 256,28 268,20 282,26 296,18 312,22 326,16 342,20 356,12 372,16 388,10 404,14 420,8 436,6 445,2 445,230 0,230"/>
  </svg>

  <p class="promo promo-lead">Visit our website for our complete<br>appetizer, pasta, salad and catering menu</p>
  <p class="promo promo-url">www.calderpizza.ca</p>
  <p class="promo promo-address">Fenwick Ridge Plaza<br>417, 318 9 Avenue SW</p>
</section>

</body>
</html>
```